Brightstep Dance Business Card

I'm looking for a two-sided business card design to promote my country dance busness. Cowboy hats, boots, and wood grain floor textures, are all appropriate to use.
On one side I want it to say:
Brightstep Dance
with
Mark
Take The Challenge - Experience The Growth
210-555-0143
On the other side I want:
A place for a Head Shot
The Quote: Experience Is The Best Teacher
A two column bullet list with the following:
First column: Two Step, Waltz, Triple Two, Polka
Second column: Cha-Cha, West Coast, East Cost, NightClub
My Name: Mark Delway
My Phone Number: 210-555-0143

```html
<!DOCTYPE html>
<html lang="en">
<head>
<meta charset="utf-8">
<title>Brightstep Dance – Business Card</title>
<link rel="stylesheet" href="https://fonts.googleapis.com/css2?family=Dancing+Script:wght@500;600&family=Lora:ital@1&family=Oswald:wght@600&family=Montserrat:wght@600;800&display=swap">
<style>
  :root {
    --canvas: #e3e3e5;
    --card: #d8955a;
    --card-light: #eab784;
    --ink: #3a1b0c;
    --ink-soft: #5a2f18;
    --art: #8a5a35;
    --art-dark: #5a3219;
    --portrait-bg: #efbf8a;
    --portrait-deep: #c98f5c;
    --list-text: #f3d3ad;
  }
  * { box-sizing: border-box; margin: 0; padding: 0; }
  html, body { width: 1200px; height: 800px; overflow: hidden; }
  body { background: var(--canvas); position: relative; }

  .card {
    position: absolute;
    top: 245px;
    width: 540px;
    height: 309px;
    background: var(--card);
    border-radius: 18px;
    overflow: hidden;
    box-shadow: 0 10px 24px rgba(0,0,0,.18);
    color: var(--ink);
  }
  .card--front { left: 40px; }
  .card--back { left: 620px; }

  .card__texture {
    position: absolute; left: 0; right: 0; bottom: 0; height: 48%;
    background: linear-gradient(to top, var(--card-light) 0%, rgba(234,183,132,.55) 45%, rgba(234,183,132,0) 100%);
  }

  /* Front */
  .front__art {
    position: absolute; left: 0; top: 90px; width: 240px; height: 219px;
    background: linear-gradient(135deg, var(--art) 0%, var(--art-dark) 100%);
    border-top-right-radius: 24px;
  }
  .front__text {
    position: absolute; left: 255px; top: 14px; width: 270px;
    text-align: center;
  }
  .brand__small { font-family: "Dancing Script", cursive; font-weight: 500; font-size: 28px; line-height: 1; }
  .brand__large { font-family: "Dancing Script", cursive; font-weight: 600; font-size: 72px; line-height: .9; }
  .brand__with { font-family: "Montserrat", sans-serif; font-weight: 600; font-size: 9px; letter-spacing: 2px; margin: 2px 0; }
  .brand__name { font-family: "Dancing Script", cursive; font-weight: 600; font-size: 54px; line-height: .95; }
  .tagline { font-family: "Lora", serif; font-style: italic; font-size: 15px; line-height: 1.3; margin-top: 8px; color: var(--ink-soft); }

  .phone {
    display: flex; align-items: center; gap: 6px;
    font-family: "Oswald", sans-serif; font-weight: 600; line-height: 1;
    color: var(--ink);
  }
  .front__phone { justify-content: center; font-size: 30px; margin-top: 8px; }
  .phone svg { flex: none; }

  /* Back */
  .back__portrait {
    position: absolute; left: 55px; top: 50px; width: 170px; height: 170px;
    border-radius: 50%;
    background: radial-gradient(circle at 50% 40%, var(--portrait-bg) 0%, var(--portrait-deep) 100%);
  }
  .back__name {
    position: absolute; left: 25px; top: 232px; width: 230px; text-align: center;
    font-family: "Dancing Script", cursive; font-weight: 600; font-size: 40px; line-height: 1.1;
  }
  .back__info { position: absolute; left: 262px; top: 34px; width: 260px; }
  .quote {
    font-family: "Montserrat", sans-serif; font-weight: 800; font-size: 21px; line-height: 1;
    text-transform: uppercase; color: var(--ink);
  }
  .quote__lead { font-size: 18px; display: block; letter-spacing: .5px; }
  .styles {
    margin-top: 8px; background: var(--ink); border-radius: 4px;
    padding: 10px 12px; display: grid; grid-template-columns: 1fr 1fr; gap: 0 10px;
    list-style: none;
  }
  .styles li {
    display: flex; align-items: center; gap: 5px;
    font-family: "Montserrat", sans-serif; font-weight: 600; font-size: 13px; line-height: 1.55;
    color: var(--list-text);
  }
  .back__phone { font-size: 34px; margin-top: 14px; }
</style>
</head>
<body>

<section class="card card--front" aria-label="Business card front">
  <div class="card__texture" role="img" aria-label="Distressed wood grain floor texture"></div>
  <div class="front__art" role="img" aria-label="Sketched cowboy hat illustration"></div>
  <div class="front__text">
    <div class="brand__small">Brightstep</div>
    <div class="brand__large">Dance</div>
    <div class="brand__with">WITH</div>
    <div class="brand__name">Mark</div>
    <p class="tagline">Take The Challenge<br>Experience The Growth</p>
    <div class="phone front__phone">
      <svg width="22" height="22" viewBox="0 0 24 24" aria-hidden="true"><path d="M6.6 10.8a15 15 0 0 0 6.6 6.6l2.2-2.2a1 1 0 0 1 1-.25 11.4 11.4 0 0 0 3.6.57 1 1 0 0 1 1 1V20a1 1 0 0 1-1 1A17 17 0 0 1 3 4a1 1 0 0 1 1-1h3.5a1 1 0 0 1 1 1c0 1.25.2 2.45.57 3.57a1 1 0 0 1-.25 1z" fill="none" stroke="currentColor" stroke-width="1.8"/></svg>
      <span>210-555-0143</span>
    </div>
  </div>
</section>

<section class="card card--back" aria-label="Business card back">
  <div class="card__texture" role="img" aria-label="Distressed wood grain floor texture"></div>
  <div class="back__portrait" role="img" aria-label="Head shot area"></div>
  <div class="back__name">Mark Delway</div>
  <div class="back__info">
    <h2 class="quote"><span class="quote__lead">Experience is the</span>Best Teacher</h2>
    <ul class="styles">
      <li><svg width="12" height="12" viewBox="0 0 12 12" aria-hidden="true"><rect x="1" y="1" width="10" height="10" fill="none" stroke="currentColor" stroke-width="1.4"/><path d="M3 6l2 2 4-4.5" fill="none" stroke="currentColor" stroke-width="1.6"/></svg>Two Step</li>
      <li><svg width="12" height="12" viewBox="0 0 12 12" aria-hidden="true"><rect x="1" y="1" width="10" height="10" fill="none" stroke="currentColor" stroke-width="1.4"/><path d="M3 6l2 2 4-4.5" fill="none" stroke="currentColor" stroke-width="1.6"/></svg>Cha-Cha</li>
      <li><svg width="12" height="12" viewBox="0 0 12 12" aria-hidden="true"><rect x="1" y="1" width="10" height="10" fill="none" stroke="currentColor" stroke-width="1.4"/><path d="M3 6l2 2 4-4.5" fill="none" stroke="currentColor" stroke-width="1.6"/></svg>Waltz</li>
      <li><svg width="12" height="12" viewBox="0 0 12 12" aria-hidden="true"><rect x="1" y="1" width="10" height="10" fill="none" stroke="currentColor" stroke-width="1.4"/><path d="M3 6l2 2 4-4.5" fill="none" stroke="currentColor" stroke-width="1.6"/></svg>West Coast</li>
      <li><svg width="12" height="12" viewBox="0 0 12 12" aria-hidden="true"><rect x="1" y="1" width="10" height="10" fill="none" stroke="currentColor" stroke-width="1.4"/><path d="M3 6l2 2 4-4.5" fill="none" stroke="currentColor" stroke-width="1.6"/></svg>Triple Two</li>
      <li><svg width="12" height="12" viewBox="0 0 12 12" aria-hidden="true"><rect x="1" y="1" width="10" height="10" fill="none" stroke="currentColor" stroke-width="1.4"/><path d="M3 6l2 2 4-4.5" fill="none" stroke="currentColor" stroke-width="1.6"/></svg>East Cost</li>
      <li><svg width="12" height="12" viewBox="0 0 12 12" aria-hidden="true"><rect x="1" y="1" width="10" height="10" fill="none" stroke="currentColor" stroke-width="1.4"/><path d="M3 6l2 2 4-4.5" fill="none" stroke="currentColor" stroke-width="1.6"/></svg>Polka</li>
      <li><svg width="12" height="12" viewBox="0 0 12 12" aria-hidden="true"><rect x="1" y="1" width="10" height="10" fill="none" stroke="currentColor" stroke-width="1.4"/><path d="M3 6l2 2 4-4.5" fill="none" stroke="currentColor" stroke-width="1.6"/></svg>NightClub</li>
    </ul>
    <div class="phone back__phone">
      <svg width="24" height="24" viewBox="0 0 24 24" aria-hidden="true"><path d="M6.6 10.8a15 15 0 0 0 6.6 6.6l2.2-2.2a1 1 0 0 1 1-.25 11.4 11.4 0 0 0 3.6.57 1 1 0 0 1 1 1V20a1 1 0 0 1-1 1A17 17 0 0 1 3 4a1 1 0 0 1 1-1h3.5a1 1 0 0 1 1 1c0 1.25.2 2.45.57 3.57a1 1 0 0 1-.25 1z" fill="none" stroke="currentColor" stroke-width="1.8"/></svg>
      <span>210-555-0143</span>
    </div>
  </div>
</section>

</body>
</html>
```